Mesa Verde Canyon Roots Gathering Music Summit & Recital Program needs a banner design to welco...

We are looking for a banner to use as a backdrop where people can take pictures and promote the event as they upload to social media. The music conference primarily targets high school students so we are looking for a design that will attract a younger audience. The festival revolves around music appreciation in the US/Mexico border. We like the "Mesa VerdeCanyon Roots Gathering" trumpet logo on the "5th annual" design attached, but we are open to other designs.
Target Market(s)
ages 15-45
Colors
Designer to choose colors to be used in the design.

```html
<!DOCTYPE html>
<html lang="en">
<head>
<meta charset="utf-8">
<title>Mesa Verde Canyon Roots Gathering – Banner</title>
<link rel="stylesheet" href="https://fonts.googleapis.com/css2?family=Bebas+Neue&family=Bodoni+Moda:wght@800&family=Baloo+2:wght@700&family=Montserrat:wght@800&display=swap">
<style>
  :root {
    --page-bg: #6b6b6b;
    --purple-light: #a005c2;
    --purple-mid: #86009e;
    --purple-dark: #5a006b;
    --lime: #e1ff12;
    --olive-lime: #c8d40f;
    --title-green: #3fdc68;
    --title-edge: #17a84a;
    --ink: #161616;
    --white: #ffffff;
    --illustration-orange: #f05a0a;
    --illustration-teal: #1fc99a;
  }
  * { margin: 0; padding: 0; box-sizing: border-box; }
  html, body { width: 1200px; height: 900px; overflow: hidden; background: var(--page-bg); }
  .canvas { position: relative; width: 1200px; height: 900px; }
  .banner {
    position: absolute; left: 0; top: 150px; width: 1200px; height: 600px; overflow: hidden;
    background: radial-gradient(ellipse at 30% 55%, var(--purple-light) 0%, var(--purple-mid) 45%, var(--purple-dark) 100%);
  }
  .banner-frame { position: absolute; inset: 0; }
  .instrument-art {
    position: absolute; left: 82px; top: 36px; width: 467px; height: 564px;
    border-radius: 48% 48% 0 0;
    background:
      linear-gradient(180deg, rgba(255,255,255,0.0) 0%, rgba(255,255,255,0.0) 60%, rgba(31,201,154,0.55) 100%),
      radial-gradient(ellipse at 50% 45%, var(--illustration-orange) 0%, #e09a12 40%, rgba(160,5,194,0) 75%);
  }
  .notes-art { position: absolute; }
  .notes-art.top { left: 800px; top: 0; width: 400px; height: 225px;
    background: radial-gradient(ellipse at 70% 40%, rgba(255,255,255,0.18), rgba(255,255,255,0) 70%); }
  .notes-art.bottom { left: 504px; top: 420px; width: 320px; height: 180px;
    background: radial-gradient(ellipse at 40% 60%, rgba(255,255,255,0.16), rgba(255,255,255,0) 70%); }
  .event-title { position: absolute; left: 590px; top: 180px; width: 550px; height: 300px; text-align: center; }
  .edition-tag {
    position: absolute; left: 141px; top: 0; width: 263px; height: 45px;
    background: var(--lime); color: var(--ink);
    font: 800 27px/45px "Montserrat", sans-serif; letter-spacing: 0.5px;
  }
  .title-main {
    position: absolute; left: 0; top: 48px; width: 550px; height: 120px; text-align: center;
    font: 400 120px/120px "Bebas Neue", sans-serif; color: var(--title-green);
    -webkit-text-stroke: 2px var(--white);
    text-shadow: 3px 3px 0 var(--title-edge), 5px 5px 0 var(--ink);
    transform: scaleX(0.6); transform-origin: center; white-space: nowrap;
  }
  .title-band {
    position: absolute; left: 15px; top: 171px; width: 521px; height: 65px;
    background: var(--olive-lime); border-radius: 3px; color: var(--ink);
    font: 800 34px/65px "Bodoni Moda", serif; letter-spacing: 6px; white-space: nowrap;
  }
  .title-sub {
    position: absolute; left: 0; top: 246px; width: 550px;
    font: 700 27px/36px "Baloo 2", sans-serif; color: var(--white); white-space: nowrap;
  }
</style>
</head>
<body>
<div class="canvas">
  <section class="banner">
    <svg class="banner-frame" width="1200" height="600" viewBox="0 0 1200 600" aria-hidden="true">
      <defs>
        <linearGradient id="frameGradient" x1="0" y1="0" x2="1" y2="0">
          <stop offset="0" stop-color="#ff1a3a"/>
          <stop offset="0.35" stop-color="#e81cff"/>
          <stop offset="0.7" stop-color="#ffb21a"/>
          <stop offset="1" stop-color="#3cf26a"/>
        </linearGradient>
      </defs>
      <rect x="19" y="20" width="1161" height="557" fill="none" stroke="url(#frameGradient)" stroke-width="3"/>
    </svg>

    <div class="notes-art top" role="img" aria-label="Flowing white music staff with notes, sharps and a treble clef"></div>
    <div class="notes-art bottom" role="img" aria-label="Flowing white music staff with scattered notes"></div>
    <div class="instrument-art" role="img" aria-label="Illustration of a guitar, trumpet, microphone, cymbals and piano with white swirls"></div>

    <div class="event-title">
      <div class="edition-tag">6TH ANNUAL</div>
      <h1 class="title-main">MESA VERDE CANYON</h1>
      <div class="title-band">ROOTS GATHERING</div>
      <p class="title-sub">Music Summit &amp; Recital Program</p>
    </div>
  </section>
</div>
</body>
</html>
```